Business Card

I need a business card for my work as an energy lawyer. I am a single prctioner and I consult to energy companies regarding a variety of legal issues involving environmental matters, energy efficiency, regulations and contractual arrangements. i need a distinctive business card that stands out and is easy to read. I like bold colors or high contrast. I like a sparse architectural design. The font should be easy to read (many of my clients use reading glasses and are concerned about small type). The card should communicate that I am somewhat different from ordinary legal counsel. Below are some examples of cards that I like. Thank you for your interest and thought. Glenn Dusty Harker
Updates

Thanks to everyone who has submitted a design.  My general comments are:

1.  I like the colourful cards and the high contrast cards.
2.  I prefer the use of icons for home address, phone, mobile and email.
3.  For the high contrast cards please use three colours - black background, and red and white for the logo or information.
4.  The mobile number area code should be 403 and not 404.
5.  I also need to add a direct phone line which is 403-517-6392.

Thank you,

Glenn Harker

Reason: I have briefly extended the deadline by three days to allow those individuals who responded early to revise their designs based upon the subsequent clarification of the colours (red, white, black background) and the request to use icons and add a direct phone number.

Industry/Entity Type

Business

```html
<!DOCTYPE html>
<html lang="en">
<head>
<meta charset="utf-8">
<title>Glenn Dusty Harker – Business Card</title>
<link rel="stylesheet" href="https://fonts.googleapis.com/css2?family=Open+Sans:wght@400;700&display=swap">
<style>
  :root {
    --backdrop: #e8e8e8;
    --card-black: #231f20;
    --card-red: #ec1c24;
    --card-white: #ffffff;
    --shadow: rgba(0, 0, 0, 0.18);
  }
  * { box-sizing: border-box; margin: 0; padding: 0; }
  html, body {
    width: 1200px;
    height: 900px;
    overflow: hidden;
    background: var(--backdrop);
    font-family: "Open Sans", Arial, sans-serif;
  }
  .canvas { position: relative; width: 1200px; height: 900px; }

  .card {
    position: absolute;
    width: 560px;
    height: 320px;
    box-shadow: 0 6px 18px var(--shadow);
    overflow: hidden;
  }

  /* Front */
  .card-front {
    left: 90px;
    top: 110px;
    background: var(--card-black);
    display: flex;
    align-items: center;
    justify-content: center;
  }
  .front-mark {
    display: flex;
    flex-direction: column;
    align-items: center;
    gap: 18px;
    color: var(--card-red);
    font-weight: 700;
    font-size: 32px;
    letter-spacing: 0.5px;
  }
  .mark-ring {
    width: 64px;
    height: 64px;
    border: 5px solid var(--card-red);
    border-radius: 50%;
    flex: none;
  }

  /* Back */
  .card-back {
    left: 550px;
    top: 470px;
    display: flex;
  }
  .back-brand {
    width: 36%;
    background: var(--card-black);
    display: flex;
    flex-direction: column;
    align-items: center;
    justify-content: center;
    gap: 12px;
    color: var(--card-white);
    font-weight: 700;
    font-size: 17px;
    text-align: center;
    line-height: 1.25;
  }
  .back-brand .mark-ring {
    width: 84px;
    height: 84px;
    border-width: 6px;
    border-color: var(--card-white);
  }
  .back-details {
    flex: 1;
    background: var(--card-red);
    color: var(--card-white);
    padding: 44px 20px 0 26px;
  }
  .holder-name { font-weight: 700; font-size: 23px; line-height: 1.1; }
  .holder-title { font-size: 13px; margin-top: 4px; }
  .contact-list { list-style: none; margin-top: 22px; }
  .contact-item {
    display: flex;
    align-items: center;
    gap: 10px;
    font-size: 14px;
    line-height: 1;
    margin-bottom: 9px;
    white-space: nowrap;
  }
  .contact-icon { width: 18px; height: 18px; flex: none; }
</style>
</head>
<body>
<main class="canvas">

  <section class="card card-front" aria-label="Card front">
    <div class="front-mark">
      <span class="mark-ring"></span>
      <span>Glenn Dusty Harker</span>
    </div>
  </section>

  <section class="card card-back" aria-label="Card back">
    <div class="back-brand">
      <span class="mark-ring"></span>
      <span>Glenn Dusty<br>Harker</span>
    </div>
    <div class="back-details">
      <h1 class="holder-name">Glenn Dusty Harker</h1>
      <p class="holder-title">Barrister and Solicitor, JD, C.Dir</p>
      <ul class="contact-list">
        <li class="contact-item">
          <svg class="contact-icon" viewBox="0 0 18 18" aria-hidden="true"><path d="M9 2 L1 9 H3.5 V16 H7.5 V11.5 H10.5 V16 H14.5 V9 H17 Z" fill="#fff"/></svg>
          2240 9th Avenue N.E., Ridgemont, Manitoba
        </li>
        <li class="contact-item">
          <svg class="contact-icon" viewBox="0 0 18 18" aria-hidden="true"><circle cx="9" cy="9" r="8" fill="none" stroke="#fff" stroke-width="1.5"/><path d="M6 4.5 L7.6 6.8 L6.8 8 Q7.8 10 10 11.2 L11.2 10.4 L13.5 12 L12.4 13.5 Q8.5 13.5 5 9 Q4.5 6 6 4.5 Z" fill="#fff"/></svg>
          1 204 681 2294
        </li>
        <li class="contact-item">
          <svg class="contact-icon" viewBox="0 0 18 18" aria-hidden="true"><rect x="5" y="1.5" width="8" height="15" rx="1.6" fill="none" stroke="#fff" stroke-width="1.6"/><circle cx="9" cy="13.6" r="1" fill="#fff"/></svg>
          1 204 839 4105
        </li>
        <li class="contact-item">
          <svg class="contact-icon" viewBox="0 0 18 18" aria-hidden="true"><circle cx="9" cy="9" r="8" fill="#fff"/></svg>
          403 517 6392
        </li>
        <li class="contact-item">
          <svg class="contact-icon" viewBox="0 0 18 18" aria-hidden="true"><circle cx="9" cy="9" r="8" fill="none" stroke="#fff" stroke-width="1.5"/><rect x="4.5" y="6" width="9" height="6.5" fill="none" stroke="#fff" stroke-width="1.2"/><path d="M4.5 6 L9 9.8 L13.5 6" fill="none" stroke="#fff" stroke-width="1.2"/></svg>
          glenn@harkerlaw.com
        </li>
      </ul>
    </div>
  </section>

</main>
</body>
</html>
```